Crew Mellow Downgraders and Upgraders Leaflets part 2

Would like to create two double-sided dl card leaflets. This is for an Australian real estate company.

1. Will be to target older people in our area. The down sizers. What do they say when we speak to them – the yard is getting too big, we cant look after the gardens any more. So idea is

Headings could be;
Is Time You Gave Your Mower A Rest?
Give your Mower A Rest
Time To Sell The Lawn Mower?

Call Crew MELLOW. We can Help You

2. Will be to target Upgraders.
Headings could be;
The house too small, kids growing up. Need to find a bigger
Kids Growing Up, Need a Home with More Space?

Call Crew MELLOW, We can Help you

One the back can we have something about Crew Mellow
Please do not forget to include contact numbers for Crew Mellow Members

**We need to Incorporate Crew MELLOW logo, stock photos (not so American) to depict the people of the two cards, and our team photo.
for more info, please see profile pages for Ludo - http://qxvantro.com.au/about/our-team/profile.aspx?sid=41fa9c3d-b7e2-4d10-a6c5-2e9b7f014a83&name=Ludo-Werensky
Tomek - http://qxvantro.com.au/about/our-team/profile.aspx?sid=c803d7e1-9a2f-4c6b-8e15-7d3a60b2f918&name=Tomek-Harbusch

We also have started using this description on our marketing products;
Crew MELLOW is a group of young enthusiastic individuals, living and breathing real estate 24/7. We love what we do and we do what we say. We work from our hearts, and our goal is to create a lasting presence, when we are not present. We hope you too will love experiencing the MELLOW difference.

Industry/Entity Type

Real Estate

```html
<!DOCTYPE html>
<html lang="en">
<head>
<meta charset="utf-8">
<title>Crew Mellow – Contact Card</title>
<link rel="stylesheet" href="https://fonts.googleapis.com/css2?family=Kalam:wght@400&family=Open+Sans:wght@400&display=swap">
<style>
  :root {
    --paper: #ffffff;
    --ink: #1f1f1f;
    --footer-ink: #6f7f95;
    --brand-yellow: #f7c244;
    --brand-dark: #1d1d1d;
    --divider: #f2b632;
  }
  * { margin: 0; padding: 0; box-sizing: border-box; }
  html, body { width: 1200px; height: 2448px; overflow: hidden; background: var(--paper); }
  .card { position: relative; width: 1200px; height: 2448px; background: var(--paper); font-family: "Kalam", cursive; color: var(--ink); }
  .contact { position: absolute; left: 407px; }
  .contact p { position: absolute; left: 0; white-space: nowrap; line-height: 1; }
  .contact .name { font-size: 66px; text-decoration: underline; text-decoration-thickness: 3px; text-underline-offset: 6px; }
  .contact .role, .contact .label, .contact .value { font-size: 50px; }
  .contact--ludo { top: 228px; }
  .contact--tomek { top: 1058px; }
  .footer-brand { position: absolute; left: 20px; top: 2232px; width: 493px; height: 112px; background: var(--brand-dark); display: flex; align-items: center; padding-left: 36px; gap: 24px; }
  .footer-brand .mark { width: 34px; height: 34px; background: var(--brand-yellow); }
  .footer-brand .brand-name { font-family: "Kalam", cursive; font-size: 58px; line-height: 1; color: #ffffff; }
  .footer-band { position: absolute; left: 529px; top: 2232px; width: 641px; height: 112px; background: var(--brand-yellow); }
  .footer-details { position: absolute; left: 78px; top: 2372px; display: flex; align-items: center; gap: 24px; font-family: "Open Sans", sans-serif; font-size: 19px; color: var(--footer-ink); white-space: nowrap; }
  .footer-details .sep { width: 4px; height: 30px; background: var(--divider); }
</style>
</head>
<body>
<main class="card">
  <section class="contact contact--ludo">
    <p class="name" style="top:0">Ludo Werensky</p>
    <p class="role" style="top:70px">director</p>
    <p class="label" style="top:180px">Phone</p>
    <p class="value" style="top:234px">08 9136 4087</p>
    <p class="label" style="top:344px">Mobile</p>
    <p class="value" style="top:398px">0431 607 219</p>
    <p class="label" style="top:508px">Email</p>
    <p class="value" style="top:562px">ludo@qxvantro.com.au</p>
  </section>

  <section class="contact contact--tomek">
    <p class="name" style="top:0">Tomek Harbusch</p>
    <p class="role" style="top:70px">Director</p>
    <p class="label" style="top:180px">Phone</p>
    <p class="value" style="top:234px">08 9136 4087</p>
    <p class="label" style="top:344px">Mobile</p>
    <p class="value" style="top:398px">0427 815 360</p>
    <p class="label" style="top:508px">Email</p>
    <p class="value" style="top:562px">tomek@qxvantro.com.au</p>
  </section>

  <div class="footer-brand">
    <span class="mark"></span>
    <span class="brand-name">Crew Mellow</span>
  </div>
  <div class="footer-band" role="img" aria-label="Brand colour band with faint company name decoration"></div>

  <footer class="footer-details">
    <span>48 Elmridge Avenue, Kewdale WA 6105</span>
    <span class="sep"></span>
    <span>mail@qxvantro.com.au</span>
    <span class="sep"></span>
    <span>9136 4087</span>
    <span class="sep"></span>
    <span>qxvantro.com.au</span>
  </footer>
</main>
</body>
</html>
```